New E-Learning Website Design Wanted!

I am creating an E-learning website for those interested in getting certifications in the IT industry.
For example, courses related to BKX, Pellin, RTM certifications and national certifications in the IT industry in Japan will be offered.
You can think of sites such as Pindoval, Fevly, VexaPoint, Bintorum.
But I am targeting industries in Japan at the moment.
Also, I have uploaded screenshots of pages that I think are good.

The company is Solvik Data
I recently got my company logo designed so I attached pdf file to this project brief.
I would appreciate it if you can make the site match the color scheme of the logo.

Target Market(s)

I am targeting individuals as well as large IT companies in Japan

Industry/Entity Type

Education

Coding

Coded - Design and coding required

Number of Pages Required

4 page

Font styles to use
Sans Serif

Colors

Designer to choose colors to be used in the design.

Requirements
Must have
• One top page design
• One course page (https://vexapt.test/courses/pellor-grid-systems)
• One learning page(where the learner can see the video)
• One blog page(https://news.vexapt.test/resources?_ga=2.36414185.89678801.1578174478-594719062.1578174478)
Nice to have
• Pricing page

```html
<!DOCTYPE html>
<html lang="en">
<head>
<meta charset="utf-8">
<title>Solvik Data – Self Education Resources</title>
<link href="https://fonts.googleapis.com/css2?family=Montserrat:wght@400;500;700;800&family=Roboto:ital,wght@0,400;0,500;0,700;1,400;1,500&display=swap" rel="stylesheet">
<style>
:root{
  --teal:#23a197;
  --teal-dark:#1b8c84;
  --blue:#1e5b8c;
  --navy:#1d4f7c;
  --text:#6b7785;
  --light:#eef5fb;
  --pale:#f4f7fa;
  --white:#ffffff;
  --star:#f5b301;
}
*{box-sizing:border-box;margin:0;padding:0}
html,body{width:1200px;height:4488px;overflow:hidden}
body{position:relative;background:var(--white);font-family:'Roboto',sans-serif;color:var(--text)}
.abs{position:absolute}
a{color:inherit;text-decoration:none}

/* hero */
.hero{left:0;top:0;width:1200px;height:710px;background:linear-gradient(160deg,#239f95 0%,#1f7f91 50%,#1e5b8c 100%)}
.brand{display:flex;align-items:center;gap:10px;color:var(--white);font-family:'Montserrat',sans-serif;font-weight:500;font-size:24px;letter-spacing:1px}
.brand-dot{width:14px;height:14px;border-radius:50%;background:var(--white)}
.topbar{top:36px;right:100px;display:flex;gap:26px;align-items:center;color:var(--white);font-size:13px}
.flag{display:inline-block;width:30px;height:16px;background:#e9eef5;vertical-align:middle;margin-left:6px}
.cart{width:38px;height:38px;border:2px solid var(--white);border-radius:50%;position:relative;display:flex;align-items:center;justify-content:center}
.cart-badge{position:absolute;top:-10px;right:-8px;width:22px;height:22px;border-radius:50%;background:#e8413c;font-size:11px;display:flex;align-items:center;justify-content:center}
.nav{top:94px;left:564px;display:flex;gap:46px;color:var(--white);font-size:14px;font-weight:700}
.nav .active{position:relative}
.nav .active::after{content:"";position:absolute;left:-4px;right:-4px;bottom:-12px;height:2px;background:var(--white)}
.hero-title{left:108px;top:228px;font-family:'Montserrat',sans-serif;font-weight:500;font-size:66px;color:var(--white);letter-spacing:3px}
.hero-sub{left:109px;top:314px;font-size:26px;font-weight:500;color:var(--white)}
.btn{display:inline-flex;align-items:center;justify-content:center;font-size:13px;font-weight:700;text-transform:uppercase;color:var(--white);background:var(--teal);border-radius:2px}
.btn-light{background:var(--white);color:var(--teal);left:112px;top:366px;width:122px;height:48px;font-size:14px}
.blob{border-radius:42% 58% 48% 52% / 40% 44% 56% 60%}
.hero-photo{left:680px;top:183px;width:348px;height:305px;background:linear-gradient(135deg,#8a7865,#4a5660 60%,#2f3b44)}
.dots{left:1136px;top:312px;display:flex;flex-direction:column;gap:8px}
.dots span{width:12px;height:12px;border-radius:50%;background:rgba(255,255,255,.5)}
.dots span:first-child{background:var(--white)}

/* about */
.feature{display:flex;flex-direction:column;align-items:center;text-align:center;padding:0 22px;border-radius:4px;background:var(--white);box-shadow:0 2px 10px rgba(0,0,0,.12);color:var(--navy);justify-content:center}
.feature h4{font-size:13px;font-weight:700;margin:16px 0 10px;line-height:1.5}
.feature p{font-size:11.5px;line-height:1.5;color:var(--teal)}
.feature.is-teal{background:var(--teal);color:var(--white)}
.feature.is-teal p,.feature.is-blue p{color:var(--white)}
.feature.is-blue{background:var(--blue);color:var(--white)}
.section-title{font-family:'Montserrat',sans-serif;font-size:40px;color:var(--navy);font-weight:500;line-height:1.25}
.section-title b{font-weight:800}
.rule{height:2px;background:#c9d2dc;width:110px}
.about-title{left:601px;top:834px}
.about-rule{left:570px;top:896px;width:120px}
.para{font-size:13.5px;line-height:26px;color:var(--text)}

/* courses */
.courses-bg{left:0;top:1254px;width:1200px;height:700px}
.courses-title{left:0;width:1200px;top:1392px;text-align:center}
.courses-rule{left:560px;top:1454px;width:80px}
.provider{top:1492px;height:60px;display:flex;align-items:center;justify-content:center;gap:10px;font-family:'Montserrat',sans-serif;font-weight:700;font-size:32px;color:var(--navy);width:312px}
.provider i{width:14px;height:14px;background:var(--navy);display:block}
.course{background:var(--white);box-shadow:0 2px 10px rgba(0,0,0,.12);border-radius:4px;width:312px}
.course-photo{height:186px;border-radius:4px 4px 0 0}
.course-body{padding:24px 36px 0}
.course-body h3{font-size:18px;font-weight:700;color:var(--navy);line-height:26px;margin-bottom:12px}
.course-body p{font-size:12.5px;line-height:22px;color:var(--text);margin-bottom:14px}
.course .btn{width:158px;height:46px;font-size:12.5px}
.course .btn-blue{background:var(--blue)}

/* business */
.biz-title{left:112px;top:2148px}
.biz-rule{left:92px;top:2266px;width:120px}
.biz-photo{left:676px;top:2146px;width:348px;height:305px;background:linear-gradient(150deg,#7b8a98,#3f5f82 55%,#2b3f5c)}
.biz-shadow{left:650px;top:2190px;width:330px;height:270px;background:#eef2f6}
.play{left:826px;top:2258px;width:52px;height:52px;border-radius:50%;border:2px solid rgba(255,255,255,.8);background:rgba(35,161,151,.55)}

/* pricing */
.plans-bg{left:0;top:2552px;width:1200px;height:692px;background:var(--pale)}
.plans-title{left:0;width:1200px;top:2606px;text-align:center}
.plan{width:313px;height:410px;background:var(--white);box-shadow:0 2px 10px rgba(0,0,0,.1);border-radius:4px;text-align:center;color:var(--navy)}
.plan h3{font-size:18px;font-weight:500;line-height:26px;height:52px;margin-top:40px;display:flex;align-items:center;justify-content:center}
.plan .price{font-size:50px;font-weight:500;margin:22px 0 14px;line-height:1}
.plan ul{list-style:none;margin:0 34px}
.plan li{font-size:12.5px;color:var(--text);height:47px;line-height:47px;border-bottom:1px solid #e4e8ee;display:flex;align-items:center;justify-content:center;gap:5px}
.plan li:last-child{border-bottom:0}
.tick{width:11px;height:11px;border-radius:50%;background:var(--teal);display:inline-block;position:relative}
.tick::after{content:"";position:absolute;left:3px;top:1.5px;width:3px;height:5px;border:solid var(--white);border-width:0 1.5px 1.5px 0;transform:rotate(45deg)}
.plan .btn{width:173px;height:46px;margin-top:22px;font-size:12.5px}
.plan.is-featured{background:linear-gradient(180deg,#23a197,#1e5b8c);color:var(--white)}
.plan.is-featured h3{margin-top:20px}
.plan.is-featured li{color:var(--white);border-color:rgba(255,255,255,.3)}
.plan.is-featured .tick{background:var(--white)}
.plan.is-featured .tick::after{border-color:var(--teal)}

/* testimonials */
.say-title{left:0;width:1200px;top:3330px;text-align:center}
.say-rule{left:560px;top:3393px;width:80px}
.stars{left:0;width:1200px;top:3430px;text-align:center;color:var(--star);font-size:20px;letter-spacing:3px}
.quote{left:210px;width:780px;top:3470px;text-align:center;font-style:italic;font-size:14.5px;line-height:26px;color:var(--text)}
.avatar{left:557px;top:3553px;width:88px;height:88px;border-radius:50%;background:linear-gradient(180deg,#c9ced4,#7c8894);border:3px solid var(--white);box-shadow:0 1px 6px rgba(0,0,0,.2)}
.person{left:0;width:1200px;top:3650px;text-align:center;font-style:italic;font-weight:500;font-size:20px;color:var(--navy)}
.partner{top:3733px;width:183px;height:91px;background:var(--white);box-shadow:0 2px 8px rgba(0,0,0,.1);display:flex;align-items:center;justify-content:center;gap:8px;font-size:13px;font-weight:700;color:#333;text-transform:uppercase}
.partner i{width:10px;height:10px;background:#333;display:block}

/* footer */
.footer{left:0;top:3885px;width:1200px;height:603px}
.footer-col{color:var(--white);font-size:13.5px}
.footer-col h4{font-size:20px;font-weight:500;margin-bottom:24px}
.footer-col ul{list-style:none}
.footer-col li{line-height:31px}
.footer-col li::before{content:"»";margin-right:10px}
.contact{display:flex;gap:14px;line-height:24px;margin-bottom:28px;color:var(--white);font-size:13.5px}
.vline{width:1px;height:230px;background:rgba(255,255,255,.45)}
.input{width:244px;height:40px;background:var(--white);border-radius:4px;color:#999;font-size:12px;padding:0 14px;display:flex;align-items:center}
.copy{left:0;width:1200px;top:4436px;text-align:center;color:var(--white);font-size:13px}
</style>
</head>
<body>

<!-- hero -->
<section class="abs hero">
  <div class="abs brand" style="left:112px;top:82px"><span class="brand-dot"></span>Solvik Data</div>
  <div class="abs topbar">
    <span>ENG ▾<span class="flag"></span></span>
    <span>&#128100; Login / Register</span>
    <span class="cart">
      <svg width="16" height="14" viewBox="0 0 16 14"><path d="M0 1h3l2 8h8l2-6H4" fill="none" stroke="#fff" stroke-width="1.6"/><circle cx="6" cy="12" r="1.3" fill="#fff"/><circle cx="12" cy="12" r="1.3" fill="#fff"/></svg>
      <span class="cart-badge">0</span>
    </span>
  </div>
  <nav class="abs nav">
    <a class="active">Home</a><a>Learning</a><a>Blog</a><a>Course</a><a>Certifications</a>
    <svg width="14" height="14" viewBox="0 0 14 14"><circle cx="6" cy="6" r="4.5" fill="none" stroke="#fff" stroke-width="2"/><path d="M9.5 9.5 13 13" stroke="#fff" stroke-width="2"/></svg>
  </nav>
  <h1 class="abs hero-title">Solvik Data</h1>
  <p class="abs hero-sub">Self Education Resources and Infos</p>
  <a class="abs btn btn-light">Get Started</a>
  <div class="abs blob hero-photo" role="img" aria-label="Person working on a laptop at a desk with a coffee cup"></div>
  <div class="abs dots"><span></span><span></span><span></span><span></span></div>
  <svg class="abs" style="left:0;top:500px" width="1200" height="212" viewBox="0 0 1200 212">
    <path d="M0 205 C150 195 300 20 420 25 C540 30 600 190 760 180 C900 170 1050 60 1200 80 L1200 212 L0 212Z" fill="#fff"/>
  </svg>
</section>

<!-- about -->
<section>
  <div class="abs feature is-teal" style="left:112px;top:740px;width:203px;height:215px">
    <svg width="56" height="46" viewBox="0 0 56 46"><rect x="2" y="2" width="52" height="32" rx="2" fill="none" stroke="#fff" stroke-width="3"/><path d="M22 44h12M28 34v10" stroke="#fff" stroke-width="3"/><text x="17" y="25" fill="#fff" font-size="18" font-family="Roboto,sans-serif" font-weight="700">$</text><path d="M31 12l9 9-4 0 2 4-2 1-2-4-3 3z" fill="#fff"/></svg>
    <h4>100,000 online courses</h4>
    <p>Explore a variety of fresh topics</p>
  </div>
  <div class="abs feature" style="left:329px;top:763px;width:206px;height:216px">
    <svg width="52" height="52" viewBox="0 0 52 52"><circle cx="22" cy="22" r="17" fill="none" stroke="#1d4f7c" stroke-width="4"/><path d="M34 34l14 14" stroke="#1d4f7c" stroke-width="5" stroke-linecap="round"/><path d="M14 22l6 6 10-11" fill="none" stroke="#23a197" stroke-width="3.5"/></svg>
    <h4>Expert instruction</h4>
    <p>Find the right instructor for you</p>
  </div>
  <div class="abs feature" style="left:112px;top:972px;width:203px;height:216px">
    <svg width="56" height="56" viewBox="0 0 56 56"><circle cx="25" cy="26" r="21" fill="none" stroke="#1d4f7c" stroke-width="3"/><path d="M25 12v14l8 6" fill="none" stroke="#1d4f7c" stroke-width="3"/><path d="M40 32l10 4v8c0 5-5 9-10 10-5-1-10-5-10-10v-8z" fill="#1d4f7c"/></svg>
    <h4>Lifetime access</h4>
    <p>Learn on your schedule</p>
  </div>
  <div class="abs feature is-blue" style="left:329px;top:996px;width:206px;height:216px">
    <svg width="58" height="46" viewBox="0 0 58 46"><g fill="#fff"><circle cx="10" cy="8" r="5"/><circle cx="29" cy="6" r="6"/><circle cx="48" cy="8" r="5"/><rect x="5" y="15" width="10" height="22" rx="4"/><rect x="23" y="14" width="12" height="28" rx="5"/><rect x="43" y="15" width="10" height="22" rx="4"/></g></svg>
    <h4>Learn from industry experts</h4>
    <p>Select from top instructors around the world</p>
  </div>
  <h2 class="abs section-title about-title"><b>ABOUT</b> SOLVIK DATA</h2>
  <div class="abs rule about-rule"></div>
  <p class="abs para" style="left:601px;top:916px;width:485px">Lorem ipsum dolor sit amet, consectetur adipiscing elit, sed do eiusmod tem por incididunt ut labore et dolore magna aliqua. Ut enim ad minim veni am, quis nostrud exercitation ullamco laboris nisi ut aliquip ex ea commodo consequat. Duis aute irure dolor in reprehenderit in voluptate velit esse cillum dolore eu fugiat nulla pariatur. Excepteur sint occaecat cupidatat non proident, sunt in culpa qui officia deserunt mollit anim id est laborum.</p>
  <a class="abs btn" style="left:601px;top:1097px;width:131px;height:49px">Read More »</a>
</section>

<!-- popular courses -->
<section>
  <svg class="abs courses-bg" width="1200" height="700" viewBox="0 0 1200 700">
    <path d="M0 0 C200 20 320 120 560 90 C780 60 900 30 1200 40 L1200 690 C1000 660 700 700 400 680 C250 670 100 690 0 680Z" fill="#eef5fb"/>
  </svg>
  <h2 class="abs section-title courses-title"><b>POPULAR</b> COURSES</h2>
  <div class="abs rule courses-rule"></div>
  <div class="abs provider" style="left:108px">BKX</div>
  <div class="abs provider" style="left:443px"><i></i>Pellin</div>
  <div class="abs provider" style="left:777px">RTM</div>

  <article class="abs course" style="left:108px;top:1576px;height:379px">
    <div class="course-photo" role="img" aria-label="Students studying together at a table with laptops" style="background:linear-gradient(135deg,#cfd6dc,#7a8a96)"></div>
    <div class="course-body">
      <h3>Lorem ipsum dolor sit amet, consectetur adipiscing</h3>
      <p>adipiscing elit, sed do eiusmod tempor incididunt ut labore et dolore magna ali qua. Ut enim ad minim veniam</p>
      <a class="btn">More Courses »</a>
    </div>
  </article>
  <article class="abs course" style="left:443px;top:1576px;height:424px">
    <div class="course-photo" role="img" aria-label="Learner with headphones taking notes at a laptop" style="background:linear-gradient(135deg,#e6e2da,#9a9c98)"></div>
    <div class="course-body">
      <h3>Lorem ipsum dolor sit amet, consectetur adipiscing</h3>
      <p>adipiscing elit, sed do eiusmod tempor incididunt ut labore et dolore magna ali qua. Ut enim ad minim veniam</p>
      <a class="btn btn-blue">More Courses »</a>
    </div>
  </article>
  <article class="abs course" style="left:777px;top:1576px;height:379px">
    <div class="course-photo" role="img" aria-label="Professional reading a phone at a laptop by a window" style="background:linear-gradient(135deg,#5e7486,#2c4257)"></div>
    <div class="course-body">
      <h3>Lorem ipsum dolor sit amet, consectetur adipiscing</h3>
      <p>adipiscing elit, sed do eiusmod tempor incididunt ut labore et dolore magna ali qua. Ut enim ad minim veniam</p>
      <a class="btn">More Courses »</a>
    </div>
  </article>
</section>

<!-- business -->
<section>
  <h2 class="abs section-title biz-title"><b>SOLVIK DATA</b> FOR<br>BUSINESS</h2>
  <div class="abs rule biz-rule"></div>
  <p class="abs para" style="left:110px;top:2278px;width:475px">Lorem ipsum dolor sit amet, consectetur adipiscing elit, sed do eiusmod tempor incididunt ut labore et dolore magna aliqua. Ut enim ad minim ve niam, quis nostrud exercitation ullamco laboris nisi ut aliquip ex ea com m odo consequat. Duis aute irure dolor in reprehenderit</p>
  <a class="abs btn" style="left:110px;top:2404px;width:132px;height:45px">Read More »</a>
  <div class="abs blob biz-shadow"></div>
  <div class="abs blob biz-photo" role="img" aria-label="Business professional using a tablet in an office"></div>
  <svg class="abs play" viewBox="0 0 52 52"><path d="M21 16l16 10-16 10z" fill="#fff"/></svg>
</section>

<!-- pricing -->
<section>
  <div class="abs plans-bg"></div>
  <h2 class="abs section-title plans-title"><b>CHOOSE THE PLAN</b><br>THAT FITS YOUR NEEDS</h2>
  <div class="abs plan" style="left:110px;top:2770px">
    <h3>PROGRAMMING<br>SUBSCRIPTION</h3>
    <div class="price">$50</div>
    <ul><li><span class="tick"></span>Lorem ipsum dolor sit amet</li><li><span class="tick"></span>Consectetur adipiscing elit dolo</li><li><span class="tick"></span>Exercitation ullamco laboris</li></ul>
    <a class="btn">Start Learning</a>
  </div>
  <div class="abs plan is-featured" style="left:442px;top:2770px">
    <h3>CLOUD SUBSCRIPTION</h3>
    <div class="price">$50</div>
    <ul><li><span class="tick"></span>Lorem ipsum dolor sit amet</li><li><span class="tick"></span>Consectetur adipiscing elit dolo</li><li><span class="tick"></span>Exercitation ullamco laboris</li></ul>
    <a class="btn">Start Learning</a>
  </div>
  <div class="abs plan" style="left:773px;top:2770px">
    <h3>ALL IN ONE<br>SUBSCRIPTION</h3>
    <div class="price">$50</div>
    <ul><li><span class="tick"></span>Lorem ipsum dolor sit amet</li><li><span class="tick"></span>Consectetur adipiscing elit dolo</li><li><span class="tick"></span>Exercitation ullamco laboris</li></ul>
    <a class="btn">Start Learning</a>
  </div>
</section>

<!-- testimonials -->
<section>
  <h2 class="abs section-title say-title"><b>WHAT OUR STUDENTS</b> HAVE TO SAY</h2>
  <div class="abs rule say-rule"></div>
  <div class="abs stars">★★★★★</div>
  <p class="abs quote">Lorem ipsum dolor sit amet, consectetur adipiscing elit, sed do eiusmod tempor incididunt ut labore et dolore magna aliqua. Ut enim ad minim veniam, quis nostrud exercitation ullamco laboris nisi ut aliquip ex ea commodo consequat. Duis aute irure dolor in reprehenderit in voluptate velit esse cillum dolore eu fugiat nulla pariatur.</p>
  <svg class="abs" style="left:68px;top:3478px" width="28" height="48" viewBox="0 0 28 48"><path d="M24 3 4 24l20 21" fill="none" stroke="#333" stroke-width="3"/></svg>
  <svg class="abs" style="left:1102px;top:3478px" width="28" height="48" viewBox="0 0 28 48"><path d="M4 3l20 21L4 45" fill="none" stroke="#333" stroke-width="3"/></svg>
  <div class="abs avatar" role="img" aria-label="Portrait photo of the student"></div>
  <div class="abs person">Daro Nell</div>
  <div class="abs partner" style="left:110px"><i></i>Company Name</div>
  <div class="abs partner" style="left:309px"><i></i>Learnhall</div>
  <div class="abs partner" style="left:507px"><i></i>Mobi Study</div>
  <div class="abs partner" style="left:706px"><i></i>Quillmark</div>
  <div class="abs partner" style="left:904px"><i></i>Tessora</div>
</section>

<!-- footer -->
<footer>
  <svg class="abs footer" width="1200" height="603" viewBox="0 0 1200 603">
    <defs><linearGradient id="footGrad" x1="0" y1="0" x2="0.3" y2="1"><stop offset="0" stop-color="#23a197"/><stop offset="1" stop-color="#1e5b8c"/></linearGradient></defs>
    <path d="M0 0 C120 60 260 150 420 120 C600 90 720 20 900 60 C1020 85 1120 40 1200 30 L1200 603 L0 603Z" fill="url(#footGrad)"/>
  </svg>
  <div class="abs brand" style="left:112px;top:4170px"><span class="brand-dot"></span>Solvik Data</div>
  <div class="abs" style="left:110px;top:4230px;width:230px">
    <div class="contact"><svg width="12" height="16" viewBox="0 0 12 16"><path d="M6 0a6 6 0 0 1 6 6c0 4-6 10-6 10S0 10 0 6a6 6 0 0 1 6-6z" fill="#fff"/><circle cx="6" cy="6" r="2" fill="#1f7f91"/></svg><span>Lorem ipsum dolor sit amet,<br>consectetur adipiscing</span></div>
    <div class="contact"><svg width="14" height="14" viewBox="0 0 14 14"><path d="M3 0l3 3-2 2c1 2 3 4 5 5l2-2 3 3-2 3C6 14 0 8 0 3z" fill="#fff"/></svg><span>+1 555 014 2290</span></div>
    <div class="contact"><svg width="16" height="12" viewBox="0 0 16 12"><rect width="16" height="12" rx="1" fill="#fff"/><path d="M0 1l8 6 8-6" fill="none" stroke="#1e6a8e" stroke-width="1.4"/></svg><span>info@solvikdata.test</span></div>
  </div>
  <div class="abs vline" style="left:362px;top:4170px"></div>
  <div class="abs footer-col" style="left:406px;top:4182px">
    <h4>Quick Links</h4>
    <ul><li>Home</li><li>Learning</li><li>Blog</li><li>Course</li><li>Certifications</li></ul>
  </div>
  <div class="abs footer-col" style="left:603px;top:4182px">
    <h4>Training</h4>
    <ul><li>BKX Courses Online</li><li>Cloud Training</li><li>BKX Certifications</li><li>BKX Certified Solutions</li><li>Architect</li></ul>
  </div>
  <div class="abs vline" style="left:810px;top:4170px"></div>
  <div class="abs footer-col" style="left:843px;top:4182px">
    <h4>Subscribe the Newsletter</h4>
    <div class="input">✉ Email Adderss</div>
    <a class="btn" style="margin-top:24px;width:124px;height:40px;font-size:11.5px;border-radius:4px">Subscribe</a>
  </div>
  <p class="abs copy">© Copyrights 2020 Solvik Data | All Rights Reserved</p>
</footer>

</body>
</html>
```